Finance Broker helping people meet their personal and business goals

New business card design,
1st look at the old business card so this makes sense.
I DON'T want:
the subtext "For all your Rural and Commercial Finance".
I DON'T want the: "and Management Consultant" words
I DON'T want the old phone: 07 48213957
I DON'T want the fax number: 07 45826031
I DON'T want the email address: tallowcreek@brightlink.com.au
I DON'T want the flower
What I DO want
I DO want the mobile 0451 836 209 (in larger text)
I DO want:
My name: Dennis Harwell-Lowe
I DO want: Australian Credit Licence 529164 (Tallow Creek Pty Ltd)
I DO want: Principal Finance Broker
I DO want new email: dennis@plotnextstep.com.au
I DO want address: PO Box 928, Tully Qld 4854
I DO want the existing logo (PNS on existing card)

Target Market(s)

Business Borrowers, Home Purchasers, and People wanting to finance cars and plant and equipment

Industry/Entity Type

Financial Service

Contact Information for Business Card

See project description

Font styles to use
Serif

Colors

Designer to choose colors to be used in the design.

Requirements
Must have
• See project description
Nice to have
• Black and Yellow colours
Should not have
• See project description

```html
<!DOCTYPE html>
<html lang="en">
<head>
<meta charset="utf-8">
<title>Plot Next Step – Business Card</title>
<link href="https://fonts.googleapis.com/css2?family=Tinos:wght@400;700&family=Open+Sans:wght@400&display=swap" rel="stylesheet">
<style>
  :root {
    --backdrop: #262626;
    --card: #121212;
    --card-edge: #1d1d1d;
    --yellow: #f5ec2a;
    --white: #ffffff;
    --muted: #e6e6e6;
  }
  * { box-sizing: border-box; margin: 0; padding: 0; }
  html, body {
    width: 1200px; height: 900px; overflow: hidden;
    background: radial-gradient(ellipse at 70% 20%, #383838 0%, var(--backdrop) 55%, #161616 100%);
  }
  .canvas { position: relative; width: 1200px; height: 900px; }
  .card {
    position: absolute; left: 250px; width: 700px; height: 400px;
    background: linear-gradient(160deg, var(--card) 0%, var(--card-edge) 100%);
    border-radius: 4px;
    box-shadow: 0 10px 30px rgba(0,0,0,0.6);
    color: var(--white);
    font-family: "Tinos", "Times New Roman", serif;
  }
  .card--front { top: 40px; }
  .card--back { top: 460px; }

  .brand { position: absolute; display: flex; align-items: center; gap: 14px; }
  .brand__text { display: flex; flex-direction: column; align-items: flex-end; }
  .brand__name {
    font-family: "Tinos", "Times New Roman", serif; font-weight: 700;
    color: var(--yellow); font-size: 36px; line-height: 1;
  }
  .brand__member {
    font-family: "Open Sans", Arial, sans-serif; font-size: 14px;
    color: var(--white); letter-spacing: 0.5px; margin-top: 4px;
  }
  .brand__dot { width: 54px; height: 54px; border-radius: 50%; background: var(--yellow); flex: none; }
  .card--front .brand { left: 120px; top: 160px; }
  .card--back .brand { right: 40px; top: 38px; }
  .card--back .brand__name { font-size: 30px; }
  .card--back .brand__member { font-size: 12px; }
  .card--back .brand__dot { width: 46px; height: 46px; }

  .holder { position: absolute; left: 52px; top: 130px; }
  .holder__name { font-size: 32px; font-weight: 700; }
  .holder__role { font-size: 18px; color: var(--muted); margin-top: 2px; }

  .licence { position: absolute; right: 44px; top: 180px; text-align: right; }
  .licence__number { font-size: 17px; color: var(--muted); }
  .licence__entity { font-size: 13px; color: var(--white); }
  .licence__entity span { color: var(--yellow); }

  .rule { position: absolute; left: 40px; right: 40px; top: 222px; height: 2px; background: var(--yellow); }

  .contacts { position: absolute; left: 44px; top: 240px; list-style: none; }
  .contacts li { display: flex; align-items: center; gap: 12px; margin-bottom: 10px; }
  .contacts svg { width: 18px; height: 18px; flex: none; fill: var(--yellow); }
  .contacts__phone { font-size: 34px; }
  .contacts__email, .contacts__address { font-size: 19px; color: var(--muted); }
</style>
</head>
<body>
<div class="canvas">

  <section class="card card--front">
    <div class="brand">
      <div class="brand__text">
        <span class="brand__name">Plot Next Step</span>
        <span class="brand__member">A Member of the Tallow Creek Group</span>
      </div>
      <span class="brand__dot"></span>
    </div>
  </section>

  <section class="card card--back">
    <div class="brand">
      <div class="brand__text">
        <span class="brand__name">Plot Next Step</span>
        <span class="brand__member">A Member of the Tallow Creek Group</span>
      </div>
      <span class="brand__dot"></span>
    </div>

    <div class="holder">
      <h1 class="holder__name">Dennis Harwell-Lowe</h1>
      <p class="holder__role">Principal Finance Broker</p>
    </div>

    <div class="licence">
      <p class="licence__number">Australian Credit Licence 529164</p>
      <p class="licence__entity">(<span>Tallow Creek Pty Ltd</span>)</p>
    </div>

    <div class="rule"></div>

    <ul class="contacts">
      <li>
        <svg viewBox="0 0 24 24" aria-hidden="true"><path d="M6.6 10.8a15.1 15.1 0 0 0 6.6 6.6l2.2-2.2c.3-.3.7-.4 1-.2 1.1.4 2.3.6 3.6.6.6 0 1 .4 1 1V20c0 .6-.4 1-1 1A17 17 0 0 1 3 4c0-.6.4-1 1-1h3.5c.6 0 1 .4 1 1 0 1.3.2 2.5.6 3.6.1.3 0 .7-.2 1z"/></svg>
        <span class="contacts__phone">0451 836 209</span>
      </li>
      <li>
        <svg viewBox="0 0 24 24" aria-hidden="true"><path d="M2 5h20v14H2zm2 2v.5l8 5 8-5V7l-8 5z"/></svg>
        <span class="contacts__email">dennis@plotnextstep.com.au</span>
      </li>
      <li>
        <svg viewBox="0 0 24 24" aria-hidden="true"><path d="M12 2a7 7 0 0 0-7 7c0 5 7 13 7 13s7-8 7-13a7 7 0 0 0-7-7zm0 9.5A2.5 2.5 0 1 1 12 6.5a2.5 2.5 0 0 1 0 5z"/></svg>
        <span class="contacts__address">PO Box 928, Tully Qld 4854</span>
      </li>
    </ul>
  </section>

</div>
</body>
</html>
```